Poster for an advertising campaign

Hi, we are an agency, our business is to orienteates student to study abroad in Germany. For that, we enroll them in language schools in Germany and help them to find an accomodation.
We are going to launch an advertising campaign through Rural advertising signs.
- Need to have our Movarel Center logo
- Need to have these 2 mentions :
1/ Etudes en Allemagne et accompagnement durant toute la procédure.
2/ Cours de langue allemande
- If possible put as a signature ; in small characters our brand essence ( Excellence Through Education ) Maybe at the bottom right of the logo
For the format it will be 3.5m*2.5m , more format adaptations will be shared as soon as we finalize the crea
- We would like to have the logo in 2D ,like for the attached simulation
- Need to have interesting backgrounds and designs in line with our identity & service ( studying in Germany , learn the German language , the support &the accompaniment during all the procedure …) ,knowing as well that our target is bachelors , bac students …
Thx

```html
<!DOCTYPE html>
<html lang="fr">
<head>
<meta charset="utf-8">
<title>Movarel Center – Etudes en Allemagne</title>
<link rel="stylesheet" href="https://fonts.googleapis.com/css2?family=Roboto+Condensed:ital,wght@0,700;1,700&display=swap">
<style>
  :root {
    --flag-black: #1b1b1d;
    --flag-red: #c8201f;
    --flag-red-deep: #9e1616;
    --flag-gold: #e5b414;
    --accent-yellow: #e4e41a;
    --text-white: #ffffff;
  }
  html, body {
    margin: 0;
    padding: 0;
    overflow: hidden;
    background: #ffffff;
  }
  .poster {
    position: relative;
    width: 1200px;
    height: 858px;
    overflow: hidden;
    font-family: "Roboto Condensed", "Arial Narrow", sans-serif;
    color: var(--text-white);
  }
  .flag-backdrop {
    position: absolute;
    inset: 0;
    background: linear-gradient(172deg,
      var(--flag-black) 0%,
      #2a2a2c 22%,
      var(--flag-red-deep) 30%,
      var(--flag-red) 40%,
      var(--flag-red) 58%,
      var(--flag-red-deep) 66%,
      #d79a14 74%,
      var(--flag-gold) 86%,
      #caa012 100%);
  }
  .brand {
    position: absolute;
    left: 60px;
    top: 168px;
    display: flex;
    align-items: center;
    gap: 18px;
  }
  .brand-dot {
    width: 46px;
    height: 46px;
    border-radius: 50%;
    background: var(--accent-yellow);
  }
  .brand-name {
    font-size: 58px;
    font-weight: 700;
    line-height: 1;
    color: var(--text-white);
    letter-spacing: 0.5px;
  }
  .headline {
    position: absolute;
    left: 464px;
    top: 244px;
    margin: 0;
    font-size: 42px;
    font-weight: 700;
    line-height: 55px;
  }
  .headline .offer {
    display: block;
    margin-top: 22px;
  }
  .service-note {
    position: absolute;
    left: 655px;
    top: 646px;
    width: 520px;
    margin: 0;
    font-size: 23px;
    font-weight: 700;
    line-height: 34px;
  }
  .brand-essence {
    position: absolute;
    right: 44px;
    top: 786px;
    margin: 0;
    font-size: 27px;
    font-weight: 700;
    font-style: italic;
  }
</style>
</head>
<body>
<main class="poster">
  <div class="flag-backdrop" role="img" aria-label="Waving German flag in black, red and gold filling the background"></div>

  <div class="brand">
    <span class="brand-dot"></span>
    <span class="brand-name">Movarel Center</span>
  </div>

  <h1 class="headline">
    Etudes en Allemagne et<br>
    accompagnement<br>
    durant toute la procédure.
    <span class="offer">Cours de langue allemande</span>
  </h1>

  <p class="service-note">studying in Germany , learn the German language , the support &amp;the accompaniment during all the procedure</p>

  <p class="brand-essence">Excellence Through Education</p>
</main>
</body>
</html>
```